Presentation Folder Design Project

We want a presentation folder design for a property business based in the UK. Our brand colour are Yellow and Black.

The background colour should be Yellow. Allowed colour are Yellow and Black and their shades.

INSIDE PAGE: 18.90 Width x 13.99 Height

OUTSIDE PAGE: 18.90 Width x 13.99 Height PLUS 4.02 Inches for the Reverse part to put papers. So that makes a total of 18.90 x 18.01 inches

The front side:
Should have company logo, company name "Kestrelmoor Group" with Tag line "Find Homes - Choose Kestrelmoor"
And three UK Houses Images. See attachment.

-
The Back side:
Should have company logo, Head Quarter Images, Address, Website, email etc. See Attachment
Should have Phone number prominent and graphically presented.

-

The Inside (Left side):

Should have a "springbok" Image with the provided Text. See attachment.

The inside (right side)

Flap to carry papers preferably with a logo on the flap.

Reason: Still trying to get some balance

Reason: Just have some changes, we want Yellow as the dominant colour as that was not followed.

Reason: Still waiting for feedback from my team

Industry/Entity Type

Business

Requirements
Must have
• The folder must have 4 pages, and use the Logo and Images we've attached.

The Background colour should be Yellow.

The Only Colour Allowed in the entire folder are Yellow, Black and Greyish Black and the shades thereof.

No other colours should be used.

ALL DESIGNERS

Please submit your designs Inner and Outer Part as ONE SINGLE design submission.

Do not Submit them separately.

```html
<!DOCTYPE html>
<html lang="en">
<head>
<meta charset="utf-8">
<title>Kestrelmoor Group – Presentation Folder</title>
<link rel="stylesheet" href="https://fonts.googleapis.com/css2?family=Source+Sans+3:ital,wght@0,400;0,600;0,700;1,400&display=swap">
<style>
  :root {
    --yellow: #eef01c;
    --black: #121212;
    --canvas: #eceeee;
    --photo-green: #6f8a4c;
    --photo-brick: #8d5a45;
    --photo-stone: #8f947a;
    --photo-field: #c79a4b;
  }
  * { margin: 0; padding: 0; box-sizing: border-box; }
  html, body { width: 1200px; height: 1026px; overflow: hidden; }
  body {
    position: relative;
    background: var(--canvas);
    font-family: "Source Sans 3", "Myriad Pro", sans-serif;
  }
  .folder-shapes { position: absolute; left: 0; top: 0; }
  .abs { position: absolute; }

  /* Outside: front cover */
  .house-photo { top: 167px; width: 86px; height: 56px; }
  .house-photo--one { left: 562px; background: linear-gradient(180deg, #a7c2d8 0%, var(--photo-green) 45%, var(--photo-brick) 70%, #4d5e36 100%); }
  .house-photo--two { left: 653px; background: linear-gradient(180deg, #dfe8ee 0%, var(--photo-brick) 40%, #6a4437 75%, #6a6c6c 100%); }
  .house-photo--three { left: 742px; width: 84px; background: linear-gradient(180deg, #c9d6db 0%, var(--photo-stone) 40%, #d8d6c4 65%, #4f6134 100%); }

  .brand-title {
    color: var(--yellow);
    font-weight: 700;
    letter-spacing: -0.2px;
    white-space: nowrap;
  }
  .brand-tagline {
    color: var(--yellow);
    font-weight: 400;
    white-space: nowrap;
  }
  .front-title { left: 554px; width: 311px; text-align: center; top: 352px; font-size: 29px; }
  .front-tagline { left: 554px; width: 311px; text-align: center; top: 389px; font-size: 18.5px; }

  /* Outside: back cover */
  .contact-block {
    left: 330px; top: 318px; width: 140px;
    text-align: center;
    color: var(--black);
    font-size: 6.5px;
    font-weight: 700;
    line-height: 1.35;
  }
  .contact-block .helpline { margin-top: 8px; }

  .brand-mark {
    display: flex; align-items: center; gap: 5px;
    font-weight: 700;
    white-space: nowrap;
  }
  .brand-mark__square { width: 18px; height: 18px; }
  .back-mark { left: 345px; top: 420px; color: var(--black); font-size: 15px; }
  .back-mark .brand-mark__square { background: var(--black); }

  /* Inside: left page */
  .emblem-photo {
    left: 354px; top: 575px; width: 92px; height: 93px;
    border-radius: 6px;
    background: linear-gradient(180deg, #d7c08a 0%, var(--photo-field) 55%, #a67a33 100%);
  }
  .emblem-caption {
    left: 280px; width: 260px; top: 676px;
    text-align: center; color: var(--yellow);
  }
  .emblem-caption h2 { font-size: 10.5px; font-weight: 700; line-height: 1.1; }
  .emblem-caption .latin { font-size: 6.5px; font-style: italic; }
  .emblem-caption .origin { font-size: 7px; margin-top: 5px; }

  .emblem-story {
    left: 297px; top: 738px; width: 232px;
    color: var(--yellow);
    font-size: 8.8px; line-height: 1.4;
  }
  .emblem-story ul { list-style: none; margin-top: 8px; padding-left: 12px; }
  .emblem-story li::before { content: "• "; }

  /* Inside: right flap */
  .flap-mark { left: 664px; top: 740px; color: var(--black); font-size: 16px; }
  .flap-mark .brand-mark__square { background: var(--black); }
  .flap-title { left: 626px; width: 241px; text-align: center; top: 906px; font-size: 23px; }
  .flap-tagline { left: 626px; width: 241px; text-align: center; top: 937px; font-size: 14.5px; }
</style>
</head>
<body>

<svg class="folder-shapes" width="1200" height="1026" viewBox="0 0 1200 1026" aria-hidden="true">
  <rect class="back-cover" x="242" y="63" width="312" height="442" fill="var(--yellow)"/>
  <path class="front-cover" d="M554 63 H826 Q836 63 836 73 V270 Q836 284 850 289 Q865 295 865 310 V474 Q865 494 846 501 Q836 505 824 505 H554 Z" fill="var(--black)"/>
  <path class="inside-left" d="M554 535 V979 H258 Q245 979 245 966 V790 Q245 775 258 770 Q272 765 272 750 V545 Q272 535 282 535 Z" fill="var(--black)"/>
  <rect class="inside-right" x="554" y="535" width="313" height="444" fill="var(--yellow)"/>
  <polygon class="flap-band" points="626,890 867,890 867,979 612,979" fill="var(--black)"/>
</svg>

<!-- Outside: back cover -->
<div class="abs contact-block">
  <p>Head Office</p>
  <p>Unit 4, Harbourside Business Park,</p>
  <p>Millbrook Road, Leeds, LS9 4QT</p>
  <p>Website: www.kestrelmoorgroup.co.uk</p>
  <p>Email: info@kestrelmoorgroup.co.uk</p>
  <p class="helpline">24/7 Helpline 0800 123 4567</p>
</div>
<div class="abs brand-mark back-mark"><span class="brand-mark__square"></span>Kestrelmoor Group</div>

<!-- Outside: front cover -->
<div class="abs house-photo house-photo--one" role="img" aria-label="Photo of a brick UK detached house with garden"></div>
<div class="abs house-photo house-photo--two" role="img" aria-label="Photo of a UK terraced street of red-brick houses"></div>
<div class="abs house-photo house-photo--three" role="img" aria-label="Photo of a stone UK semi-detached house"></div>
<h1 class="abs brand-title front-title">Kestrelmoor Group</h1>
<p class="abs brand-tagline front-tagline">Find Homes - Choose Kestrelmoor</p>

<!-- Inside: left page -->
<div class="abs emblem-photo" role="img" aria-label="Photo of a kestrel perched above open golden moorland"></div>
<div class="abs emblem-caption">
  <h2>The Kestrel</h2>
  <p class="latin">(Falco tinnunculus)</p>
  <p class="origin">A small falcon of the open moor, famed for hovering still in the wind.</p>
</div>
<div class="abs emblem-story">
  <p>The kestrel is a small, chestnut and grey falcon, found across the UK. We chose the kestrel as our emblem because:</p>
  <ul>
    <li>It's sharp-eyed, like us. We spot the right home for you fast - often before it reaches the market!</li>
    <li>It hovers patiently, like we do while we listen and shape a plan that truly fits your needs!</li>
    <li>It moves swiftly, like we do to carry you past the usual delays, thanks to our clear, simple steps.</li>
    <li>It stays loyal to its home ground, like we stay loyal to our clients, with honesty and care guided by our charter.</li>
    <li>It thrives in every season, like our company. We're growing thanks to our knowledge, integrity and a level of service that no one can match!</li>
  </ul>
</div>

<!-- Inside: right flap -->
<div class="abs brand-mark flap-mark"><span class="brand-mark__square"></span>Kestrelmoor Group</div>
<h2 class="abs brand-title flap-title">Kestrelmoor Group</h2>
<p class="abs brand-tagline flap-tagline">Find Homes - Choose Kestrelmoor</p>

</body>
</html>
```